Improve Design and Readability of Existing Web Page

Corvantia.org is a free educational radiology resource with one of the web's largest collections of radiology cases and reference articles. This job involves improving the design of the article pages to make the text more readable.
We want a new design for the body of the article page that has considered at least: the typeface, vertical rhythm, line length, line height and styling of the text, headings and other standard HTML elements. IMPORTANT: You would only be designing the content area of the page, inside the existing layout, as indicated here: http://q.zx/i/Tk4W
If you are the successful applicant you'll have your work featured across the 6000+ article pages on the site.
The HTML elements that you will need to consider in your design are:
* Headings (three levels)
* Paragraphs
* Superscript and Subscript text
* Ordered and unordered lists, potentially nested multiple levels deep
* Links to other corvantia content (blue links)
* Links to other corvantia content that does not yet exist (grey links)
The articles are accessible at: http://corvantia.org/encyclopaedia/all/all
Sample articles that can be used for reference and as a base for the redesign:
* http://corvantia.org/articles/neurosarcoidosis
* http://corvantia.org/articles/golden_s_sign
* http://corvantia.org/articles/fetal-heart-rate
* http://corvantia.org/articles/meningioma

```html
<!DOCTYPE html>
<html lang="en">
<head>
<meta charset="utf-8">
<title>Neurosarcoidosis | Corvantia.org</title>
<style>
:root{
  --page-bg:#dcdcdc;
  --header:#15202d;
  --banner:#3a5f9e;
  --banner-dark:#2c4a80;
  --nav:#1f3153;
  --nav-tab:#2d4673;
  --ink:#2b2b2b;
  --muted:#777;
  --link:#2a62b8;
  --ghost:#9a9a9a;
  --rule:#e2e2e2;
  --panel:#f4f4f4;
  --footer:#1b1b1b;
  --footer-text:#bdbdbd;
  --tab:#3b7dd8;
}
*{box-sizing:border-box;margin:0;padding:0}
html,body{width:1200px;height:2364px;overflow:hidden}
body{background:var(--page-bg);font-family:"Helvetica Neue",Helvetica,Arial,sans-serif;color:var(--ink);position:relative}
.site-header{position:absolute;top:0;left:0;width:1200px;height:48px;background:var(--header)}
.site-header .inner{width:960px;margin:0 auto;display:flex;align-items:center;height:48px;gap:18px}
.brand{color:#fff;font-weight:700;font-size:20px;display:flex;align-items:center;gap:8px}
.brand i{width:14px;height:14px;border-radius:50%;background:#fff;display:block}
.network{color:#c9d1dc;font-size:11px}
.donate{position:absolute;top:48px;left:0;width:1200px;height:80px;background:var(--banner)}
.donate .inner{width:960px;margin:0 auto;height:80px;display:flex;align-items:center;justify-content:center;color:#fff;font-size:30px;background:var(--banner-dark)}
.main-nav{position:absolute;top:128px;left:120px;width:960px;height:42px;background:var(--nav);display:flex;align-items:center;padding-left:10px;gap:6px}
.main-nav a{color:#fff;font-size:11px;font-weight:700;text-decoration:none;padding:6px 10px;text-transform:uppercase}
.main-nav a.active{background:var(--nav-tab)}
.main-nav .add{font-size:10px;font-weight:400;color:#b8c5dd}
.main-nav .search{margin-left:auto;margin-right:10px;width:150px;height:22px;background:#fff;border-radius:2px}
.feedback{position:absolute;width:22px;height:84px;background:var(--tab);color:#fff;font-size:10px;writing-mode:vertical-rl;display:flex;align-items:center;justify-content:center}
.page{position:absolute;top:170px;left:120px;width:960px;height:1840px;background:#fff;overflow:hidden;display:flex;gap:30px;padding:24px 20px 0 24px}
.article{width:650px}
.article h1{font-size:26px;font-weight:400;margin-bottom:4px}
.byline{font-size:12px;color:var(--muted);margin-bottom:12px}
.byline a{color:var(--link);text-decoration:none}
.article h2{font-size:20px;font-weight:400;margin:22px 0 8px;padding-bottom:4px;border-bottom:1px solid var(--rule)}
.article h3{font-size:15px;font-weight:700;margin:18px 0 6px}
.article p{font-size:13.5px;line-height:21px;margin-bottom:12px}
.article ul{font-size:13.5px;line-height:21px;margin:0 0 12px 22px}
.article ul ul{margin:0 0 0 22px;list-style:circle}
.article sup{font-size:9px;line-height:0}
.article a{color:var(--link);text-decoration:none}
.article a.ghost{color:var(--ghost)}
.sidebar{width:236px}
.tools{display:flex;gap:6px;margin-bottom:10px}
.tools span{height:24px;border:1px solid #ccc;border-radius:3px;background:var(--panel);flex:1;font-size:10px;display:flex;align-items:center;justify-content:center;color:#555}
.info{border:1px solid var(--rule);background:var(--panel);font-size:11px;margin-bottom:14px}
.info h4{font-size:12px;padding:7px 9px;border-bottom:1px solid var(--rule)}
.info p{padding:5px 9px;color:#555}
.info a{color:var(--link);text-decoration:none}
.app-ad{background:#2f6cc4;color:#fff;padding:10px;margin-bottom:14px;height:150px}
.app-ad strong{display:block;font-size:16px;margin-bottom:8px}
.app-ad .screen{height:86px;background:linear-gradient(#5d8fd8,#204f96);border-radius:3px}
.gallery{display:grid;grid-template-columns:1fr 1fr;gap:8px}
.gallery figure{font-size:10px;color:#666;text-align:center}
.gallery .scan{height:104px;background:radial-gradient(circle,#9a9a9a,#2a2a2a 70%);margin-bottom:3px}
.yearly{position:absolute;top:2020px;left:120px;width:960px;height:66px;background:var(--banner);color:#fff;font-size:26px;display:flex;align-items:center;justify-content:center}
.site-footer{position:absolute;top:2100px;left:0;width:1200px;height:264px;background:var(--footer)}
.site-footer .inner{width:960px;margin:0 auto;padding-top:16px;display:grid;grid-template-columns:repeat(6,1fr);gap:14px}
.site-footer h5{color:#fff;font-size:12px;margin-bottom:8px}
.site-footer li{list-style:none;color:var(--footer-text);font-size:10px;line-height:16px}
.copyright{position:absolute;bottom:14px;left:120px;color:#777;font-size:10px}
</style>
</head>
<body>
<header class="site-header"><div class="inner"><div class="brand"><i></i>Corvantia.org</div><span class="network">Member of the Calder Medica network</span></div></header>
<div class="donate"><div class="inner">and consider donating.</div></div>
<nav class="main-nav">
  <a class="active" href="#">Encyclopaedia</a><a class="add" href="#">+ Add Article</a>
  <a href="#">Patient Cases</a><a class="add" href="#">+ Add Case</a>
  <a href="#">Quizzes</a><a href="#">Courses</a>
  <span class="search"></span>
</nav>
<div class="feedback" style="left:0;top:440px">feedback</div>
<div class="feedback" style="right:0;top:420px">feedback</div>

<main class="page">
<article class="article">
  <h1>Neurosarcoidosis</h1>
  <p class="byline"><a href="#">Dr Miles Harrow</a> and <a href="#">Dr Anton Vell</a> et al.</p>
  <p>Central nervous system involvement by sarcoidosis (also termed neurosarcoidosis) is relatively common among patients with <a href="#">systemic sarcoidosis</a>, and has a bewildering variety of manifestations, often making diagnosis difficult.</p>
  <p>For a general discussion of the underlying condition, please refer to the article <a href="#">sarcoidosis</a>.</p>

  <h2>Epidemiology</h2>
  <p>The demographics of affected patients is not different to that of systemic sarcoidosis, typically affecting patients 30-40 years of age with a female predilection<sup>1</sup>. Histologically, central nervous system involvement is seen in 14-27% of patients with systemic sarcoidosis, although only 5-15% are symptomatic<sup>1,2</sup>. Interestingly, up to 50% of patients with systemic disease will demonstrate imaging findings, thus not all patients with demonstrable imaging findings of neurosarcoidosis are symptomatic.</p>
  <p>Disease limited to the central nervous system (i.e. isolated neurosarcoidosis) is rare, with incidence ranging between series from 1-10%<sup>1,2</sup>.</p>

  <h2>Clinical presentation</h2>
  <p>Central nervous system involvement by sarcoidosis is very variable, with lesions potentially involving the leptomeninges, pituitary and parenchyma of all parts of the intracranial compartment. Thus clinical presentation is also very variable and non-specific. It includes:</p>
  <ul>
    <li>signs and symptoms of raised ICP due to <a href="#">hydrocephalus</a></li>
    <li>cranial nerve palsies
      <ul><li>optic nerve involvement (particularly common)<sup>1</sup></li><li>facial nerve palsy</li></ul></li>
    <li><a href="#">diabetes insipidus</a> from pituitary involvement</li>
    <li>seizures</li>
    <li>variable weakness, paresthesiae and dysesthesia / dysphasia</li>
    <li>spinal cord involvement presenting as myelopathy<sup>3</sup></li>
  </ul>
  <p>Although it is very rare to have isolated neurosarcoidosis (i.e. without systemic disease), central nervous system symptoms are not uncommonly the first manifestation, with up to half of patients are often managed without the diagnosis of systemic sarcoidosis having yet been made.</p>

  <h2>Radiographic features</h2>
  <p>The radiographic features of neurosarcoidosis can be thought of as occurring in one or more of five compartments. From superficial to deep they are:</p>
  <ul>
    <li>skull vault involvement (refer to <a class="ghost" href="#">musculoskeletal manifestations of sarcoidosis</a>)</li>
    <li>pachymeningeal involvement</li>
    <li>leptomeningeal involvement (seen in up to 40% of cases<sup>1</sup>)
      <ul><li>pituitary and hypothalamic involvement</li><li>cranial nerve involvement</li></ul></li>
    <li>parenchymal involvement (most common)</li>
  </ul>

  <h3>CT</h3>
  <p>Although CT is usually the first modality used in the work up of patients with neurosarcoidosis, it is not as sensitive or specific as MRI, with up to 60% of patients with subsequently proven neurosarcoidosis having negative CT scans<sup>1</sup>. The features will be similar and regions that demonstrate enhancement on MRI may also be seen to enhance on CT, although often less dramatically.</p>
  <p>On non-contrast scanning lesions, be they pachymeningeal, leptomeningeal or parenchymal, can appear hyperdense<sup>1</sup>.</p>
  <p>Often the only finding is <a href="#">hydrocephalus</a> due to unseen leptomeningeal disease<sup>1</sup>.</p>

  <h3>MRI</h3>
  <p>MRI with contrast is the modality of choice for investigating suspected neurosarcoidosis. In general lesions follow a standard signal intensity<sup>1,2</sup>:</p>
  <ul>
    <li>T1: iso or hypo-intense with respect to adjacent grey matter</li>
    <li>T2
      <ul><li>variable</li><li>most are hyper-intense</li><li>some lesions can be iso or hypo-intense</li></ul></li>
    <li>T1 C+ (Gd): homogeneous enhancement</li>
  </ul>
  <p>Leptomeningeal disease typically shows smooth or nodular enhancement along the basal cisterns, and may extend along the perivascular spaces into the adjacent brain parenchyma<sup>2</sup>.</p>
</article>

<aside class="sidebar">
  <div class="tools"><span>Edit article</span><span>Share</span><span>Print</span></div>
  <div class="info"><h4>Article information</h4><p>System: <a href="#">Central Nervous System</a></p><p>Tag: <a href="#">neurology</a></p></div>
  <div class="app-ad"><strong>Corvantia.org mobile app</strong><div class="screen" role="img" aria-label="App screenshot on a blue gradient"></div></div>
  <div class="gallery">
    <figure><div class="scan" role="img" aria-label="Axial MRI brain"></div>Case 1</figure>
    <figure><div class="scan" role="img" aria-label="Axial MRI brain with contrast"></div>Case 2</figure>
    <figure><div class="scan" role="img" aria-label="Sagittal MRI brain"></div>Case 3</figure>
    <figure><div class="scan" role="img" aria-label="Coronal MRI brain"></div>Case 4</figure>
    <figure><div class="scan" role="img" aria-label="MRI spine"></div>Case 5</figure>
    <figure><div class="scan" role="img" aria-label="MRI pituitary"></div>Case 6</figure>
    <figure><div class="scan" role="img" aria-label="CT brain"></div>Case 7</figure>
    <figure><div class="scan" role="img" aria-label="MRI orbits"></div>Case 8</figure>
  </div>
</aside>
</main>

<div class="yearly">Only once a year...</div>
<div class="feedback" style="left:0;top:2150px">feedback</div>
<div class="feedback" style="right:0;top:2100px">feedback</div>

<footer class="site-footer">
  <div class="inner">
    <div><h5>Encyclopaedia</h5><ul><li>Anatomy</li><li>Breast</li><li>Cardiac</li><li>Chest</li><li>Gastrointestinal</li><li>Gynaecology</li><li>Head and neck</li><li>Musculoskeletal</li></ul></div>
    <div><h5>By System</h5><ul><li>Breast</li><li>Central nervous</li><li>Hepatobiliary</li><li>Obstetrics</li><li>Oncology</li><li>Paediatrics</li><li>Spine</li><li>Urogenital</li></ul></div>
    <div><h5>&nbsp;</h5><ul><li>Trauma</li><li>Vascular</li><li>Haematology</li><li>Interventional</li><li>Forensic</li><li>Physics</li></ul></div>
    <div><h5>Patient Cases</h5><ul><li>Recent cases</li><li>Add a case</li><li>Case of the day</li><li>Quiz cases</li><li>Playlists</li></ul></div>
    <div><h5>&nbsp;</h5><ul><li>Musculoskeletal</li><li>Obstetrics</li><li>Paediatrics</li><li>Spine</li><li>Vascular</li></ul></div>
    <div><h5>About Corvantia.org</h5><ul><li>Blog</li><li>Editorial board</li><li>Donate</li><li>Terms of use</li><li>Privacy policy</li><li>Licensing</li><li>Contact</li></ul></div>
  </div>
  <p class="copyright">Copyright © Corvantia.org. All rights reserved.</p>
</footer>
</body>
</html>
```